HIgh-end jewelry designer needs a business card design

I need a business card design for the ecclectic & rather expensive jewelry designs. My approach to my work is to combine very old jewelry offset with contemporary items. I enjoy the idea of legacy as well as repurposing finely crafted items that are not possible to create any longer. My desire is to celebrate the past in a contemporary & funky way. The name of my business is VELLORINE. I see my business card design as simple & yet enigmatic as possible. In the end... clean, simple & understated is the look I am after. Thank you for your consideration...

Target Market(s)

I will use this business card for the trade as well as customers

Industry/Entity Type

Business

Contact Information for Business Card

Marta Quorrin Owner/Designer 555-203-7718

Requirements
Must have
• Clean & simple sophisticated design using the word "Vellorinne" as the logo. I like the idea of a play on the word itself, perhaps even using different fonts (i.e.: a bold helvetica combined with a lovely script). I'm afraid to say more because I don't want to limit creative input. Gosh, sometimes it's ok to break the rules!
Nice to have
• In my mind, I have imagined this business card to be simple, using my company name "Vellorine" in a playful yet sophisticated manner. I believe that doing something beautifully simple can be a true challenge. I have imagined something with just black & white, however I am open to ideas... after all that's why I'm here!
Should not have
• As Mozart once said... "It has too many notes!" I know I'm being silly, but I don't want it to be complicated or overly ornate.

```html
<!DOCTYPE html>
<html lang="en">
<head>
<meta charset="utf-8">
<title>Vellorine — Business Cards</title>
<link rel="stylesheet" href="https://fonts.googleapis.com/css2?family=Tenor+Sans&display=swap">
<style>
  :root {
    --stage: #cec4c3;
    --card-dark: #1f1f1f;
    --card-light: #ffffff;
    --ink-light: #ffffff;
    --ink-dark: #111111;
    --contact-on-dark: #8c8c8c;
    --contact-on-light: #7c7c7c;
    --mark-on-dark: #ffffff;
    --mark-on-light: #444444;
  }
  html, body {
    margin: 0;
    padding: 0;
    width: 1200px;
    height: 1000px;
    overflow: hidden;
    background: var(--stage);
  }
  .canvas {
    position: relative;
    width: 1200px;
    height: 1000px;
    font-family: "Tenor Sans", "Optima", sans-serif;
  }
  .card {
    position: absolute;
    width: 701px;
    height: 400px;
    box-sizing: border-box;
  }
  .card--dark { left: 251px; top: 84px; background: var(--card-dark); }
  .card--light { left: 250px; top: 521px; background: var(--card-light); }

  .brand-name {
    position: absolute;
    left: 188px;
    top: 36px;
    margin: 0;
    font-size: 30px;
    font-weight: 400;
    letter-spacing: 0.56em;
    line-height: 1;
  }
  .card--dark .brand-name { color: var(--ink-light); }
  .card--light .brand-name { color: var(--ink-dark); }

  .contact-line {
    position: absolute;
    right: 25px;
    bottom: 28px;
    margin: 0;
    font-size: 17px;
    letter-spacing: 0.09em;
    line-height: 1;
    white-space: nowrap;
  }
  .card--dark .contact-line { color: var(--contact-on-dark); }
  .card--light .contact-line { color: var(--contact-on-light); }

  .corner-mark {
    position: absolute;
    left: 24px;
    bottom: 27px;
    width: 16px;
    height: 16px;
  }
  .card--dark .corner-mark circle { stroke: var(--mark-on-dark); }
  .card--light .corner-mark circle { stroke: var(--mark-on-light); }
</style>
</head>
<body>
<main class="canvas">
  <section class="card card--dark">
    <h1 class="brand-name">VELLORINE</h1>
    <svg class="corner-mark" viewBox="0 0 16 16" aria-hidden="true">
      <circle cx="8" cy="8" r="7" fill="none" stroke-width="1.2"/>
    </svg>
    <p class="contact-line">MARTA QUORRIN . OWNER &amp; DESIGNER . 555-203-7718</p>
  </section>

  <section class="card card--light">
    <h1 class="brand-name">VELLORINE</h1>
    <svg class="corner-mark" viewBox="0 0 16 16" aria-hidden="true">
      <circle cx="8" cy="8" r="7" fill="none" stroke-width="1.2"/>
    </svg>
    <p class="contact-line">MARTA QUORRIN . OWNER &amp; DESIGNER . 555-203-7718</p>
  </section>
</main>
</body>
</html>
```